We need a full website with logo/graphics/woocommerce for hemp-based company

This site will be velmorix.com. It is a website featuring the fact we are the only manufacturer to produce CBDP and THCP. It should be great on mobile and desktop. We will pay for any extensions needed and while it should be a simple site:

About Us
About the Laboratory
About CBDP
About THCP
Shop
Contact Us

Only 4 products on the site.

It can be wordpress or joomla. Your choice. You must install the final website on our server. We agree to pay for monthly support that must be submitted in your quote.

He have a great graphics designer that will assist keeping colors and graphics clean according to your specifications.

Industry/Entity Type

Hemp CBD THC

Coding

Coded - Design and coding required

Number of Pages Required

5+ page

Requirements
Must have
• A simple clean layout

```html
<!DOCTYPE html>
<html lang="en">
<head>
<meta charset="utf-8">
<title>Velmorix – Home</title>
<link rel="stylesheet" href="https://fonts.googleapis.com/css2?family=Roboto:wght@400;500;700;900&family=Catamaran:wght@700;800&display=swap">
<style>
:root{
  --green:#1a9b4f;
  --green-dark:#148242;
  --ink:#1d1d1d;
  --muted:#777;
  --line:#e4e4e4;
  --soft:#f5f5f5;
  --footer:#2c2c2c;
  --amber:#c98a3a;
}
*{box-sizing:border-box;margin:0;padding:0}
html,body{width:1200px;height:3741px;overflow:hidden}
body{position:relative;background:#fff;font-family:"Roboto",sans-serif;color:var(--ink)}
.abs{position:absolute}
svg{display:block}

/* top bar */
.topbar{position:absolute;left:0;top:0;width:1200px;height:38px;border-bottom:1px solid var(--line);font-size:12px;color:#444}
.topbar .promo{position:absolute;left:24px;top:11px}
.topbar .info{position:absolute;right:22px;top:11px;display:flex;gap:16px;align-items:center}
.topbar .info span{display:flex;gap:6px;align-items:center}

/* header */
.header{position:absolute;top:38px;left:0;width:1200px;height:106px}
.brand{position:absolute;left:23px;top:14px;display:flex;align-items:center;gap:10px}
.brand .mark{width:50px;height:50px;border-radius:50%;background:var(--green)}
.brand .name{font-family:"Catamaran",sans-serif;font-weight:800;font-size:33px;color:var(--green);line-height:1}
.brand .tag{font-size:8.5px;font-weight:700;color:#333;margin-top:2px}
.nav{position:absolute;left:321px;top:48px;display:flex;gap:17px;font-size:14.5px;font-weight:500;color:#222}
.nav .active{color:var(--green)}
.hotline{position:absolute;left:946px;top:30px;display:flex;gap:18px;align-items:center}
.hotline .txt{font-size:11.5px;color:var(--green);line-height:17px}
.hotline .txt b{font-weight:700}

/* category bar */
.catbar{position:absolute;top:144px;left:0;width:1200px;height:52px;background:var(--green);color:#fff}
.catbar .label{position:absolute;left:19px;top:15px;font-size:17px;font-weight:700}
.catbar .burger{position:absolute;left:199px;top:17px}
.search{position:absolute;left:254px;top:11px;width:575px;height:31px;background:#fff;display:flex}
.search .field{flex:1;font-size:13.5px;color:#777;padding:8px 14px}
.search .select{width:150px;font-size:13.5px;color:#666;padding:8px 0;display:flex;justify-content:space-between;padding-right:12px}
.search .go{width:54px;background:#333;display:flex;align-items:center;justify-content:center}
.catbar .cart{position:absolute;left:1072px;top:16px;font-size:15px;font-weight:700;display:flex;gap:8px;align-items:center}

/* mini strip */
.strip{position:absolute;top:196px;left:0;width:1200px;height:90px;background:var(--soft)}
.mini{position:absolute;top:13px;display:flex;gap:14px}
.mini .thumb{width:78px;height:64px;background:radial-gradient(ellipse 30% 45% at 50% 55%,var(--amber),#f3ece2 80%,#fff);border:1px solid #eee}
.mini .t{font-size:11.5px;font-weight:700;margin-top:10px}
.mini .p{font-size:10.5px;color:#999;margin-top:5px}

/* hero */
.ph{position:absolute}
.ph-lab{left:41px;top:334px;width:729px;height:446px;background:linear-gradient(160deg,#3a3a3a,#6a5a44 45%,#2f68b8 70%,#b5572a)}
.ph-reactor{left:786px;top:334px;width:385px;height:205px;background:linear-gradient(180deg,#6d7374,#c9cccc 50%,#8b9090)}
.ph-oil{left:786px;top:555px;width:385px;height:205px;background:radial-gradient(ellipse at 40% 50%,#c9c26a,#7b7a58 55%,#3c3a2c)}

/* features */
.feature{position:absolute;top:867px;display:flex;gap:12px}
.feature h4{font-size:13px;font-weight:700;margin-top:2px}
.feature p{font-size:11.5px;color:#666;margin-top:6px}

/* section titles */
.title{position:absolute;left:0;width:1200px;text-align:center;font-family:"Catamaran",sans-serif;font-weight:800;font-size:32px;color:#111}
.sub{position:absolute;left:0;width:1200px;text-align:center;font-size:13.5px;color:#999}

.ph-vessel{left:38px;top:1100px;width:564px;height:767px;background:linear-gradient(180deg,#5c6062,#a9adae 40%,#8a8f90 70%,#4f5355)}

/* product cards */
.card{position:absolute}
.card .thumb{background:radial-gradient(ellipse 22% 42% at 50% 55%,var(--amber),#e9d7bd 60%,#fafafa 90%)}
.card .thumb.green{background:radial-gradient(ellipse 22% 42% at 50% 55%,#1f6b3a,#cfe0d3 60%,#fafafa 90%)}
.card .thumb.blue{background:radial-gradient(ellipse 22% 42% at 50% 55%,#9b5b2a,#dde4ee 60%,#fafafa 90%)}
.card .thumb.dark{background:radial-gradient(ellipse 30% 42% at 40% 55%,#2a2a2a,#e3dcd8 60%,#fafafa 90%)}
.card .name{position:absolute;left:0;font-size:8.5px;font-weight:700;color:#333;white-space:nowrap}
.card .price{position:absolute;left:0;font-size:12px;color:#555}
.card .actions{position:absolute;left:0;display:flex;align-items:center}
.btn-cart{background:var(--green);color:#fff;display:flex;align-items:center;justify-content:center;gap:6px;font-size:11px}
.btn-wish{background:#eee;color:#888;display:flex;align-items:center;justify-content:space-between;padding:0 8px;font-size:10.5px}

.lab .thumb{width:262px;height:218px}
.lab .name{top:258px}.lab .price{top:283px}
.lab .actions{top:315px}
.lab .btn-cart{width:118px;height:25px}
.lab .btn-wish{width:118px;height:25px;margin-left:12px}

.latest .thumb{width:200px;height:203px}
.latest .name{top:233px}.latest .price{top:256px}
.latest .actions{top:291px}
.latest .btn-cart{width:93px;height:27px;font-size:10.5px}
.latest .btn-wish{width:96px;height:27px;margin-left:11px;padding:0 5px}

.rated .thumb{width:200px;height:217px}
.rated .name{top:253px;font-size:11px}.rated .price{top:276px}
.rated .actions{top:310px}
.rated .btn-cart{width:91px;height:27px;font-weight:700;font-size:11px}
.rated .btn-wish{width:96px;height:27px;margin-left:13px;padding:0 5px}

/* brands */
.brandtile{position:absolute;top:3156px;width:180px;text-align:center}
.brandtile .thumb{margin:0 auto;width:60px;height:106px;background:radial-gradient(ellipse 40% 45% at 50% 60%,var(--amber),#efe1c9 70%,#fff)}
.brandtile .bn{font-family:"Catamaran",sans-serif;font-weight:800;font-size:21px;margin-top:38px;color:#222}

/* footer */
.footer{position:absolute;left:0;top:3346px;width:1200px;height:395px;background:var(--footer);color:#fff}
.footnav{position:absolute;top:53px;left:0;width:1200px;display:flex;justify-content:center;gap:26px;font-size:14.5px;font-weight:700}
.footer p{position:absolute;top:124px;left:195px;width:810px;text-align:center;font-size:14px;line-height:25px}
.social{position:absolute;top:245px;left:0;width:1200px;display:flex;justify-content:center;gap:20px}
.social span{width:26px;height:26px;border-radius:50%;border:1.5px solid #fff}
.copy{position:absolute;top:311px;width:1200px;text-align:center;font-size:11px}
.pay{position:absolute;top:342px;left:0;width:1200px;display:flex;justify-content:center;gap:9px}
.pay span{width:45px;height:30px;background:#3c6fb5;border-radius:3px}
.pay span:nth-child(2n){background:#d9dde3}
.totop{position:absolute;left:1131px;top:300px;width:34px;height:34px;background:#f3f3f3;border:1px solid #bbb;display:flex;align-items:center;justify-content:center}
</style>
</head>
<body>

<div class="topbar">
  <div class="promo">Get 50% Off In Every Products - New Year 2021 Deals</div>
  <div class="info">
    <span><svg width="14" height="12" viewBox="0 0 14 12"><rect x="1" y="4" width="12" height="7" fill="#555"/><rect x="4" y="1" width="6" height="4" fill="#555"/></svg>Sydney, Australia</span>
    <span><svg width="16" height="12" viewBox="0 0 16 12"><rect x="0" y="2" width="10" height="7" fill="#555"/><path d="M10 4h3l3 3v2h-6z" fill="#555"/><circle cx="3" cy="10" r="2" fill="#555"/><circle cx="12" cy="10" r="2" fill="#555"/></svg>Free Delivery / Cash on Delivery</span>
  </div>
</div>

<header class="header">
  <div class="brand">
    <div class="mark"></div>
    <div>
      <div class="name">VELMORIX</div>
      <div class="tag">THE ONLY PURVEYORS OF CBDP AND THCP</div>
    </div>
  </div>
  <nav class="nav">
    <span class="active">HOME</span><span>ABOUT THE LABORATORY</span><span>ABOUT CBDP</span><span>ABOUT THCP</span><span>SHOP</span><span>CONTACT</span>
  </nav>
  <div class="hotline">
    <svg width="42" height="42" viewBox="0 0 42 42"><path d="M8 24v-4a13 13 0 0 1 26 0v4" fill="none" stroke="var(--green)" stroke-width="4"/><rect x="5" y="21" width="8" height="12" rx="3" fill="var(--green)"/><rect x="29" y="21" width="8" height="12" rx="3" fill="var(--green)"/><path d="M33 33q0 6-10 6" fill="none" stroke="var(--green)" stroke-width="3"/></svg>
    <div class="txt"><b>+1 404 555 0187</b><br>info@velmorix.com</div>
  </div>
</header>

<div class="catbar">
  <div class="label">MAIN CATEGORIES</div>
  <svg class="burger" width="16" height="14" viewBox="0 0 16 14"><rect y="0" width="16" height="2.5" fill="#fff"/><rect y="5.5" width="16" height="2.5" fill="#fff"/><rect y="11" width="16" height="2.5" fill="#fff"/></svg>
  <div class="search">
    <div class="field">Search products</div>
    <div class="select"><span>All Categories</span><span>⌄</span></div>
    <div class="go"><svg width="13" height="13" viewBox="0 0 13 13"><circle cx="5.5" cy="5.5" r="4" fill="none" stroke="#fff" stroke-width="2"/><path d="M8.5 8.5l3.5 3.5" stroke="#fff" stroke-width="2"/></svg></div>
  </div>
  <div class="cart">CART <svg width="20" height="17" viewBox="0 0 20 17"><path d="M1 1h3l2 10h11l2-7H5" fill="none" stroke="#fff" stroke-width="1.6"/><circle cx="8" cy="14.5" r="1.5" fill="#fff"/><circle cx="15" cy="14.5" r="1.5" fill="#fff"/></svg></div>
</div>

<div class="strip">
  <div class="mini" style="left:23px"><div class="thumb" role="img" aria-label="Product bottle"></div><div><div class="t">Nova Phone 12</div><div class="p" style="color:#333;font-weight:500">$2,000.00</div></div></div>
  <div class="mini" style="left:246px"><div class="thumb" role="img" aria-label="Product bottle"></div><div><div class="t">Loresm ipsum dolor sit</div><div class="p">$ 30.00</div></div></div>
  <div class="mini" style="left:488px"><div class="thumb" role="img" aria-label="Product bottle"></div><div><div class="t">Loresm ipsum dolor sit</div><div class="p">$ 30.00</div></div></div>
  <div class="mini" style="left:712px"><div class="thumb" role="img" aria-label="Product bottle"></div><div><div class="t">Loresm ipsum dolor sit</div><div class="p">$ 30.00</div></div></div>
  <div class="mini" style="left:940px"><div class="thumb" role="img" aria-label="Product bottle"></div><div><div class="t">Loresm ipsum dolor sit</div><div class="p">$ 30.00</div></div></div>
</div>

<div class="ph ph-lab" role="img" aria-label="Gloved hand holding a vial of oil beneath a lab dispensing machine"></div>
<div class="ph ph-reactor" role="img" aria-label="Row of glass reactor vessels in the laboratory"></div>
<div class="ph ph-oil" role="img" aria-label="Close-up of golden oil inside a glass flask"></div>

<div class="feature" style="left:41px"><svg width="30" height="22" viewBox="0 0 30 22"><rect x="0" y="3" width="18" height="13" fill="var(--green)"/><path d="M18 7h6l5 5v4H18z" fill="var(--green)"/><circle cx="6" cy="18" r="3" fill="var(--green)"/><circle cx="23" cy="18" r="3" fill="var(--green)"/></svg><div><h4>Home Delivery</h4><p>Get your order at your door steps</p></div></div>
<div class="feature" style="left:291px"><svg width="30" height="22" viewBox="0 0 30 22"><circle cx="10" cy="6" r="5" fill="var(--green)"/><circle cx="21" cy="6" r="4" fill="var(--green)"/><path d="M0 20a10 8 0 0 1 20 0z" fill="var(--green)"/><path d="M17 13a9 7 0 0 1 13 7h-8z" fill="var(--green)"/></svg><div><h4>Online Support</h4><p>Get top notch 24/7 help</p></div></div>
<div class="feature" style="left:509px"><svg width="24" height="24" viewBox="0 0 24 24"><path d="M2 10h5v12H2zM8 10l5-8c2 0 3 1 2 4l-1 3h7c2 0 2 2 1 3l-3 9H8z" fill="none" stroke="var(--green)" stroke-width="2"/></svg><div><h4>Customer Satisfaction</h4><p>100% grunteed services</p></div></div>
<div class="feature" style="left:758px"><svg width="28" height="24" viewBox="0 0 28 24"><path d="M2 9h6l14-7v20L8 15H2z" fill="var(--green)"/><path d="M6 15l3 8h3l-2-8" fill="var(--green)"/></svg><div><h4>Great Deals</h4><p>Get upto 80% off</p></div></div>
<div class="feature" style="left:940px"><svg width="28" height="24" viewBox="0 0 28 24"><path d="M1 2h4l3 14h15l3-10H7" fill="none" stroke="var(--green)" stroke-width="2"/><path d="M9 9h15M10 12h13" stroke="var(--green)" stroke-width="1.5"/><circle cx="10" cy="20" r="2" fill="var(--green)"/><circle cx="21" cy="20" r="2" fill="var(--green)"/></svg><div><h4>Easy Pay</h4><p>COD / online payment available</p></div></div>

<h2 class="title" style="top:988px">PRODUCTS DIRECT FROM OUR LAB</h2>
<div class="sub" style="top:1043px">Get Upto Flat 80% Off On Selected Products</div>

<div class="ph ph-vessel" role="img" aria-label="Large glass reaction vessel with steel frame"></div>

<div class="card lab" style="left:629px;top:1119px"><div class="thumb" role="img" aria-label="Water soluble oil dropper bottle"></div><div class="name">LORESM IPSUM DOLOR SIT</div><div class="price">$159.00</div><div class="actions"><span class="btn-cart">ADD TO CART <svg width="15" height="13" viewBox="0 0 20 17"><path d="M1 1h3l2 10h11l2-7H5" fill="none" stroke="#fff" stroke-width="1.8"/><circle cx="8" cy="14.5" r="1.5" fill="#fff"/><circle cx="15" cy="14.5" r="1.5" fill="#fff"/></svg></span><span class="btn-wish">Add To Wishlist <svg width="12" height="11" viewBox="0 0 12 11"><path d="M6 11L1 6a3 3 0 0 1 5-4 3 3 0 0 1 5 4z" fill="var(--green)"/></svg></span></div></div>
<div class="card lab" style="left:910px;top:1119px"><div class="thumb" role="img" aria-label="Water soluble oil dropper bottle"></div><div class="name">LORESM IPSUM DOLOR SIT</div><div class="price">$30.00</div><div class="actions"><span class="btn-cart">ADD TO CART <svg width="15" height="13" viewBox="0 0 20 17"><path d="M1 1h3l2 10h11l2-7H5" fill="none" stroke="#fff" stroke-width="1.8"/><circle cx="8" cy="14.5" r="1.5" fill="#fff"/><circle cx="15" cy="14.5" r="1.5" fill="#fff"/></svg></span><span class="btn-wish">Add To Wishlist <svg width="12" height="11" viewBox="0 0 12 11"><path d="M6 11L1 6a3 3 0 0 1 5-4 3 3 0 0 1 5 4z" fill="var(--green)"/></svg></span></div></div>
<div class="card lab" style="left:629px;top:1504px"><div class="thumb" role="img" aria-label="Water soluble oil dropper bottle"></div><div class="name">LORESM IPSUM DOLOR SIT</div><div class="price">$130.00</div><div class="actions"><span class="btn-cart">ADD TO CART <svg width="15" height="13" viewBox="0 0 20 17"><path d="M1 1h3l2 10h11l2-7H5" fill="none" stroke="#fff" stroke-width="1.8"/><circle cx="8" cy="14.5" r="1.5" fill="#fff"/><circle cx="15" cy="14.5" r="1.5" fill="#fff"/></svg></span><span class="btn-wish">Add To Wishlist <svg width="12" height="11" viewBox="0 0 12 11"><path d="M6 11L1 6a3 3 0 0 1 5-4 3 3 0 0 1 5 4z" fill="var(--green)"/></svg></span></div></div>
<div class="card lab" style="left:910px;top:1504px"><div class="thumb" role="img" aria-label="Water soluble oil dropper bottle"></div><div class="name">LORESM IPSUM DOLOR SIT</div><div class="price">$250.00</div><div class="actions"><span class="btn-cart">ADD TO CART <svg width="15" height="13" viewBox="0 0 20 17"><path d="M1 1h3l2 10h11l2-7H5" fill="none" stroke="#fff" stroke-width="1.8"/><circle cx="8" cy="14.5" r="1.5" fill="#fff"/><circle cx="15" cy="14.5" r="1.5" fill="#fff"/></svg></span><span class="btn-wish">Add To Wishlist <svg width="12" height="11" viewBox="0 0 12 11"><path d="M6 11L1 6a3 3 0 0 1 5-4 3 3 0 0 1 5 4z" fill="var(--green)"/></svg></span></div></div>

<h2 class="title" style="top:1968px">LATEST PRODUCTS</h2>

<div class="card latest" style="left:42px;top:2085px"><div class="thumb green" role="img" aria-label="Green dropper bottle"></div><div class="name">LORESM IPSUM DOLOR SIT</div><div class="price">$30.00</div><div class="actions"><span class="btn-cart">Add To Cart <svg width="13" height="11" viewBox="0 0 20 17"><path d="M1 1h3l2 10h11l2-7H5" fill="none" stroke="#fff" stroke-width="1.8"/><circle cx="8" cy="14.5" r="1.5" fill="#fff"/><circle cx="15" cy="14.5" r="1.5" fill="#fff"/></svg></span><span class="btn-wish">Add To Wishlis <svg width="11" height="10" viewBox="0 0 12 11"><path d="M6 11L1 6a3 3 0 0 1 5-4 3 3 0 0 1 5 4z" fill="var(--green)"/></svg></span></div></div>
<div class="card latest" style="left:270px;top:2085px"><div class="thumb blue" role="img" aria-label="Amber dropper bottle with blue label"></div><div class="name">LORESM IPSUM DOLOR SIT</div><div class="price">$175.00</div><div class="actions"><span class="btn-cart">Add To Cart <svg width="13" height="11" viewBox="0 0 20 17"><path d="M1 1h3l2 10h11l2-7H5" fill="none" stroke="#fff" stroke-width="1.8"/><circle cx="8" cy="14.5" r="1.5" fill="#fff"/><circle cx="15" cy="14.5" r="1.5" fill="#fff"/></svg></span><span class="btn-wish">Add To Wishlis <svg width="11" height="10" viewBox="0 0 12 11"><path d="M6 11L1 6a3 3 0 0 1 5-4 3 3 0 0 1 5 4z" fill="var(--green)"/></svg></span></div></div>
<div class="card latest" style="left:498px;top:2085px"><div class="thumb dark" role="img" aria-label="Vape cartridge beside its box"></div><div class="name">LORESM IPSUM DOLOR SIT</div><div class="price">$90.00</div><div class="actions"><span class="btn-cart">Add To Cart <svg width="13" height="11" viewBox="0 0 20 17"><path d="M1 1h3l2 10h11l2-7H5" fill="none" stroke="#fff" stroke-width="1.8"/><circle cx="8" cy="14.5" r="1.5" fill="#fff"/><circle cx="15" cy="14.5" r="1.5" fill="#fff"/></svg></span><span class="btn-wish">Add To Wishlis <svg width="11" height="10" viewBox="0 0 12 11"><path d="M6 11L1 6a3 3 0 0 1 5-4 3 3 0 0 1 5 4z" fill="var(--green)"/></svg></span></div></div>
<div class="card latest" style="left:726px;top:2085px"><div class="thumb" role="img" aria-label="Water soluble oil dropper bottle"></div><div class="name">LORESM IPSUM DOLOR SIT</div><div class="price">$80.00</div><div class="actions"><span class="btn-cart">Add To Cart <svg width="13" height="11" viewBox="0 0 20 17"><path d="M1 1h3l2 10h11l2-7H5" fill="none" stroke="#fff" stroke-width="1.8"/><circle cx="8" cy="14.5" r="1.5" fill="#fff"/><circle cx="15" cy="14.5" r="1.5" fill="#fff"/></svg></span><span class="btn-wish">Add To Wishlis <svg width="11" height="10" viewBox="0 0 12 11"><path d="M6 11L1 6a3 3 0 0 1 5-4 3 3 0 0 1 5 4z" fill="var(--green)"/></svg></span></div></div>
<div class="card latest" style="left:955px;top:2085px"><div class="thumb blue" role="img" aria-label="Amber dropper bottle with blue label"></div><div class="name">LORESM IPSUM DOLOR SIT</div><div class="price">$70.00</div><div class="actions"><span class="btn-cart">Add To Cart <svg width="13" height="11" viewBox="0 0 20 17"><path d="M1 1h3l2 10h11l2-7H5" fill="none" stroke="#fff" stroke-width="1.8"/><circle cx="8" cy="14.5" r="1.5" fill="#fff"/><circle cx="15" cy="14.5" r="1.5" fill="#fff"/></svg></span><span class="btn-wish">Add To Wishlis <svg width="11" height="10" viewBox="0 0 12 11"><path d="M6 11L1 6a3 3 0 0 1 5-4 3 3 0 0 1 5 4z" fill="var(--green)"/></svg></span></div></div>

<h2 class="title" style="top:2476px;font-weight:700">Top Rated Products</h2>

<div class="card rated" style="left:42px;top:2594px"><div class="thumb blue" role="img" aria-label="Amber dropper bottle with blue label"></div><div class="name">LORESM IPSUM DOLOR SIT</div><div class="price">$159.00</div><div class="actions"><span class="btn-cart">Add To Cart <svg width="13" height="11" viewBox="0 0 20 17"><path d="M1 1h3l2 10h11l2-7H5" fill="none" stroke="#fff" stroke-width="1.8"/><circle cx="8" cy="14.5" r="1.5" fill="#fff"/><circle cx="15" cy="14.5" r="1.5" fill="#fff"/></svg></span><span class="btn-wish">Add To Wishlis <svg width="11" height="10" viewBox="0 0 12 11"><path d="M6 11L1 6a3 3 0 0 1 5-4 3 3 0 0 1 5 4z" fill="var(--green)"/></svg></span></div></div>
<div class="card rated" style="left:269px;top:2594px"><div class="thumb blue" role="img" aria-label="Amber dropper bottle with blue label"></div><div class="name">LORESM IPSUM DOLOR SIT</div><div class="price">$250.00</div><div class="actions"><span class="btn-cart">Add To Cart <svg width="13" height="11" viewBox="0 0 20 17"><path d="M1 1h3l2 10h11l2-7H5" fill="none" stroke="#fff" stroke-width="1.8"/><circle cx="8" cy="14.5" r="1.5" fill="#fff"/><circle cx="15" cy="14.5" r="1.5" fill="#fff"/></svg></span><span class="btn-wish">Add To Wishlis <svg width="11" height="10" viewBox="0 0 12 11"><path d="M6 11L1 6a3 3 0 0 1 5-4 3 3 0 0 1 5 4z" fill="var(--green)"/></svg></span></div></div>
<div class="card rated" style="left:497px;top:2594px"><div class="thumb blue" role="img" aria-label="Amber dropper bottle with blue label"></div><div class="name">LORESM IPSUM DOLOR SIT</div><div class="price">$45.00</div><div class="actions"><span class="btn-cart">Add To Cart <svg width="13" height="11" viewBox="0 0 20 17"><path d="M1 1h3l2 10h11l2-7H5" fill="none" stroke="#fff" stroke-width="1.8"/><circle cx="8" cy="14.5" r="1.5" fill="#fff"/><circle cx="15" cy="14.5" r="1.5" fill="#fff"/></svg></span><span class="btn-wish">Add To Wishlis <svg width="11" height="10" viewBox="0 0 12 11"><path d="M6 11L1 6a3 3 0 0 1 5-4 3 3 0 0 1 5 4z" fill="var(--green)"/></svg></span></div></div>
<div class="card rated" style="left:726px;top:2594px"><div class="thumb blue" role="img" aria-label="Amber dropper bottle with blue label"></div><div class="name">LORESM IPSUM DOLOR SIT</div><div class="price">$150.00</div><div class="actions"><span class="btn-cart">Add To Cart <svg width="13" height="11" viewBox="0 0 20 17"><path d="M1 1h3l2 10h11l2-7H5" fill="none" stroke="#fff" stroke-width="1.8"/><circle cx="8" cy="14.5" r="1.5" fill="#fff"/><circle cx="15" cy="14.5" r="1.5" fill="#fff"/></svg></span><span class="btn-wish">Add To Wishlis <svg width="11" height="10" viewBox="0 0 12 11"><path d="M6 11L1 6a3 3 0 0 1 5-4 3 3 0 0 1 5 4z" fill="var(--green)"/></svg></span></div></div>
<div class="card rated" style="left:954px;top:2594px"><div class="thumb blue" role="img" aria-label="Amber dropper bottle with blue label"></div><div class="name">LORESM IPSUM DOLOR SIT</div><div class="price">$65.00</div><div class="actions"><span class="btn-cart">Add To Cart <svg width="13" height="11" viewBox="0 0 20 17"><path d="M1 1h3l2 10h11l2-7H5" fill="none" stroke="#fff" stroke-width="1.8"/><circle cx="8" cy="14.5" r="1.5" fill="#fff"/><circle cx="15" cy="14.5" r="1.5" fill="#fff"/></svg></span><span class="btn-wish">Add To Wishlis <svg width="11" height="10" viewBox="0 0 12 11"><path d="M6 11L1 6a3 3 0 0 1 5-4 3 3 0 0 1 5 4z" fill="var(--green)"/></svg></span></div></div>

<h2 class="title" style="top:3082px">OUR AUTORIZED BRANDS</h2>
<div class="brandtile" style="left:193px"><div class="thumb" role="img" aria-label="Brand product bottle"></div><div class="bn">BRAND NAME</div></div>
<div class="brandtile" style="left:394px"><div class="thumb" role="img" aria-label="Brand product bottle"></div><div class="bn">BRAND NAME</div></div>
<div class="brandtile" style="left:593px"><div class="thumb" role="img" aria-label="Brand product bottle"></div><div class="bn">BRAND NAME</div></div>
<div class="brandtile" style="left:804px"><div class="thumb" role="img" aria-label="Brand product bottle"></div><div class="bn">BRAND NAME</div></div>

<footer class="footer">
  <nav class="footnav"><span>SHOP</span><span>MY ACCOUNT</span><span>CART</span><span>ABOUT CBDP</span><span>ABOUT THCP</span><span>ABOUT OUR LABRATORY</span><span>CONTACT</span></nav>
  <p>Commodo viverra maecenas accumsan lacus vel facilisis volutpat. Est velit egestas dui id ornare arcu. Erat nam at lectus urna duis. Libero nunc consequat interdum varius sit amet mattis. Nunc faucibus a pellentesque sit amet porttitor eget dolor. Amet consectetur adipiscing elit duis tristique. Mus mauris vitae ultricies leo integer. Vitae ultricies leo integer malesuada nunc vel. Venenatis cras sed felis eget velit aliquet sagittis id consectetur. Eget felis eget nunc lobortis mattis.</p>
  <div class="social"><span></span><span></span><span></span><span></span><span></span></div>
  <div class="copy">Copyright © Velmorix 2021, All Rights Reserved</div>
  <div class="totop"><svg width="12" height="14" viewBox="0 0 12 14"><path d="M6 13V2M1 6l5-5 5 5" fill="none" stroke="#333" stroke-width="1.6"/></svg></div>
  <div class="pay"><span></span><span></span><span></span><span></span><span></span><span></span><span></span><span></span></div>
</footer>

</body>
</html>
```